Business Card Design Project

it should have the logo in one side
the other side

Name
Position
telephone
email

Target Market(s)

Business prospects and upscale Fashion shoppers

Industry/Entity Type

Business

Font styles to use
Serif
Sans Serif

Requirements
Must have
• very elegant, upscale, modern
Nice to have
• layering, embossed
Should not have
• Should not use any color OTHER THAN black, silver, white or purple

```html
<!DOCTYPE html>
<html lang="en">
<head>
<meta charset="utf-8">
<title>Hartwell Business Card</title>
<link rel="stylesheet" href="https://fonts.googleapis.com/css2?family=Orbitron:wght@500&family=Oswald:wght@500&family=Montserrat:wght@400;500&display=swap">
<style>
  :root {
    --backdrop: #e8e8ea;
    --card-white: #ffffff;
    --purple-deep: #3a1d5a;
    --purple-mid: #5b3487;
    --purple-light: #7d55a8;
    --silver-light: #d9d9de;
    --silver-dark: #9a9aa3;
    --ink: #1e1e22;
    --ink-soft: #45454c;
  }
  * { margin: 0; padding: 0; box-sizing: border-box; }
  html, body {
    width: 1200px; height: 987px; overflow: hidden;
    background: var(--backdrop);
  }
  .stage {
    position: relative; width: 1200px; height: 987px;
    display: flex; justify-content: center; align-items: center; gap: 80px;
  }
  .card {
    position: relative; width: 380px; height: 640px;
    background: var(--card-white);
    box-shadow: 0 18px 40px rgba(0,0,0,0.18);
    overflow: hidden;
  }
  .card-shapes { position: absolute; inset: 0; }
  .shape-top { fill: var(--purple-deep); }
  .shape-band { fill: var(--silver-dark); }
  .stop-a { stop-color: var(--purple-light); }
  .stop-b { stop-color: var(--purple-mid); }
  .stop-c { stop-color: var(--purple-deep); }
  .brand {
    position: absolute; left: 0; right: 0; top: 220px;
    display: flex; align-items: center; justify-content: center; gap: 14px;
  }
  .brand-square {
    width: 26px; height: 26px; background: var(--purple-mid);
  }
  .brand-name {
    font-family: 'Orbitron', sans-serif; font-weight: 500;
    font-size: 34px; letter-spacing: 3px; color: var(--purple-mid);
  }
  .identity { position: absolute; left: 44px; right: 30px; top: 150px; }
  .brand-small {
    display: flex; align-items: center; justify-content: flex-end; gap: 8px;
    margin-bottom: 52px;
  }
  .brand-small .brand-square { width: 14px; height: 14px; }
  .brand-small .brand-name { font-size: 20px; letter-spacing: 2px; }
  .person-name {
    font-family: 'Oswald', sans-serif; font-weight: 500;
    font-size: 30px; letter-spacing: 1.5px; color: var(--ink); text-align: center;
  }
  .person-role {
    font-family: 'Montserrat', sans-serif; font-size: 14px; letter-spacing: 3px;
    color: var(--ink-soft); text-align: center; margin-top: 2px;
  }
  .contacts {
    list-style: none; margin-top: 34px;
    display: grid; grid-template-columns: 1fr 1fr; row-gap: 16px; column-gap: 10px;
  }
  .contacts li {
    display: flex; align-items: center; gap: 7px;
    font-family: 'Montserrat', sans-serif; font-size: 11px; color: var(--ink-soft);
    white-space: nowrap;
  }
  .contact-icon { width: 16px; height: 16px; flex: none; }
  .icon-line { fill: none; stroke: var(--ink); }
  .icon-fill { fill: var(--ink); }
  .icon-rev { fill: none; stroke: #fff; }
  .address {
    position: absolute; left: 0; right: 0; top: 540px;
    text-align: center; color: #fff;
    font-family: 'Montserrat', sans-serif; font-size: 13px; letter-spacing: 1px; line-height: 1.6;
  }
  .address-pin { width: 26px; height: 26px; display: block; margin: 0 auto 8px; }
  .pin-ring { fill: none; stroke: #fff; }
  .pin-body { fill: #fff; }
  .pin-dot { fill: var(--purple-mid); }
</style>
</head>
<body>
<main class="stage">

  <section class="card card-front" aria-label="Card front">
    <svg class="card-shapes" viewBox="0 0 380 640" width="380" height="640" aria-hidden="true">
      <defs>
        <linearGradient id="panelFront" x1="0" y1="0" x2="1" y2="1">
          <stop offset="0" class="stop-a"/>
          <stop offset="0.5" class="stop-b"/>
          <stop offset="1" class="stop-c"/>
        </linearGradient>
      </defs>
      <polygon class="shape-top" points="0,0 380,0 380,52 190,14 0,52"/>
      <polygon class="shape-band" points="0,430 190,490 380,430 380,640 0,640"/>
      <polygon points="0,444 190,504 380,444 380,640 0,640" fill="url(#panelFront)"/>
    </svg>
    <div class="brand">
      <span class="brand-square"></span>
      <span class="brand-name">HARTWELL</span>
    </div>
  </section>

  <section class="card card-back" aria-label="Card back">
    <svg class="card-shapes" viewBox="0 0 380 640" width="380" height="640" aria-hidden="true">
      <defs>
        <linearGradient id="panelBack" x1="0" y1="0" x2="1" y2="1">
          <stop offset="0" class="stop-a"/>
          <stop offset="0.5" class="stop-b"/>
          <stop offset="1" class="stop-c"/>
        </linearGradient>
      </defs>
      <polygon class="shape-top" points="0,0 380,0 380,52 190,14 0,52"/>
      <polygon class="shape-band" points="0,430 190,490 380,430 380,640 0,640"/>
      <polygon points="0,444 190,504 380,444 380,640 0,640" fill="url(#panelBack)"/>
    </svg>

    <div class="identity">
      <div class="brand-small">
        <span class="brand-square"></span>
        <span class="brand-name">HARTWELL</span>
      </div>
      <h1 class="person-name">ELLIS MARLOWE</h1>
      <p class="person-role">GENERAL MANAGER</p>
      <ul class="contacts">
        <li>
          <svg class="contact-icon" viewBox="0 0 16 16" aria-hidden="true"><circle class="icon-line" cx="8" cy="8" r="7" stroke-width="1.2"/><path class="icon-fill" d="M5.5 4.5l1.5 1.6-.8 1c.6 1.2 1.4 2 2.6 2.6l1-.8 1.6 1.5-.9 1c-2.7-.3-5.5-3.1-5.8-5.8z"/></svg>
          012 555 0147
        </li>
        <li>
          <svg class="contact-icon" viewBox="0 0 16 16" aria-hidden="true"><circle class="icon-fill" cx="8" cy="8" r="7"/><rect class="icon-rev" x="4" y="5.5" width="8" height="5" stroke-width="1"/><path class="icon-rev" d="M4 5.5l4 3 4-3" stroke-width="1"/></svg>
          ellis@hartwell.com
        </li>
        <li>
          <svg class="contact-icon" viewBox="0 0 16 16" aria-hidden="true"><circle class="icon-line" cx="8" cy="8" r="7" stroke-width="1.2"/><rect class="icon-line" x="5.8" y="3.8" width="4.4" height="8.4" rx="0.8" stroke-width="1"/><circle class="icon-fill" cx="8" cy="10.8" r="0.6"/></svg>
          012 555 0148
        </li>
        <li>
          <svg class="contact-icon" viewBox="0 0 16 16" aria-hidden="true"><circle class="icon-fill" cx="8" cy="8" r="7"/><circle class="icon-rev" cx="8" cy="8" r="4" stroke-width="0.9"/><ellipse class="icon-rev" cx="8" cy="8" rx="1.7" ry="4" stroke-width="0.9"/><path class="icon-rev" d="M4 8h8" stroke-width="0.9"/></svg>
          www.hartwellstudio.com
        </li>
      </ul>
    </div>

    <div class="address">
      <svg class="address-pin" viewBox="0 0 26 26" aria-hidden="true"><circle class="pin-ring" cx="13" cy="13" r="12" stroke-width="1.5"/><path class="pin-body" d="M13 6.5a4.3 4.3 0 0 0-4.3 4.3c0 3.2 4.3 8.2 4.3 8.2s4.3-5 4.3-8.2A4.3 4.3 0 0 0 13 6.5z"/><circle class="pin-dot" cx="13" cy="10.8" r="1.6"/></svg>
      <p>24 Alder Road</p>
      <p>3rd building Street</p>
    </div>
  </section>

</main>
</body>
</html>
```